Poster Design

Hello,

My name is Rowan Pickett and I run a vidora channel called 'CrumbleDiary'. I want a poster made for those who watch my video to purchase and put on their wall at home. The poster will be all text and as you can see, I've attached a few examples of posters which I would like it to be similar to. I use a lot of the colour #ab6f7f so it would be good to incorporate this in somewhere (maybe the background colour).
I would like the poster to say:
"Do More Of What Makes YOU Happy"
I need this poster to be for sale ready for christmas, so Im going to need the designs created as soon as possible. Im sorry for the rush.
Have fun with it and feel free to upload multiple versions of a design as well as a few designs if you like.
I look forward to seeing what you come up with.
Rowan
(Of course I will need to own all rights once the payment has been made)

```html
<!DOCTYPE html>
<html lang="en">
<head>
<meta charset="utf-8">
<title>Do More Of What Makes You Happy — Poster</title>
<link rel="stylesheet" href="https://fonts.googleapis.com/css2?family=Anton&family=Playfair+Display:wght@400&family=Ultra&family=Alfa+Slab+One&display=block">
<style>
  :root {
    --mauve: #ab6f7f;
    --mauve-deep: #8e5369;
    --mauve-light: #b78494;
    --wine: #9a4a5e;
    --shadow: rgba(70, 18, 38, 0.55);
    --white: #ffffff;
  }
  html, body {
    margin: 0;
    padding: 0;
    width: 849px;
    height: 1200px;
    overflow: hidden;
    background: var(--mauve);
  }
  .poster {
    position: relative;
    width: 849px;
    height: 1200px;
    overflow: hidden;
  }
  .poster__backdrop {
    position: absolute;
    inset: 0;
    background:
      radial-gradient(ellipse at 30% 20%, var(--mauve-light) 0%, transparent 60%),
      radial-gradient(ellipse at 75% 80%, var(--mauve-light) 0%, transparent 55%),
      linear-gradient(160deg, var(--mauve) 0%, var(--mauve-deep) 50%, var(--mauve) 100%);
  }
  .ribbon {
    position: absolute;
    left: 0;
    top: 0;
    width: 849px;
    height: 320px;
  }
  .ribbon__label {
    position: absolute;
    left: 215px;
    top: 107px;
    width: 397px;
    height: 133px;
    margin: 0;
    display: flex;
    align-items: center;
    justify-content: center;
    font-family: "Playfair Display", serif;
    font-weight: 400;
    font-size: 72px;
    letter-spacing: 1px;
    color: var(--wine);
  }
  .line {
    position: absolute;
    left: 0;
    width: 849px;
    margin: 0;
    text-align: center;
    color: var(--white);
    text-shadow: 4px 5px 5px var(--shadow);
  }
  .line--of {
    top: 266px;
    font-family: "Ultra", "Alfa Slab One", serif;
    font-size: 66px;
    line-height: 90px;
  }
  .line--what {
    top: 352px;
    font-family: "Ultra", "Alfa Slab One", serif;
    font-size: 118px;
    line-height: 150px;
  }
  .makes {
    position: absolute;
    top: 500px;
    left: 75px;
    width: 700px;
    display: flex;
    align-items: center;
    gap: 22px;
  }
  .makes__rule {
    flex: 1;
    height: 1px;
    background: var(--white);
    opacity: 0.8;
  }
  .makes__word {
    font-family: "Playfair Display", serif;
    font-size: 44px;
    line-height: 50px;
    color: var(--wine);
    -webkit-text-stroke: 1.5px var(--white);
    text-shadow: 2px 2px 3px var(--shadow);
  }
  .line--you {
    top: 520px;
    font-family: "Anton", sans-serif;
    font-size: 262px;
    line-height: 300px;
    letter-spacing: 0;
    transform: scaleX(0.88);
    transform-origin: 428px 0;
  }
  .arc {
    position: absolute;
    left: 0;
    top: 0;
    width: 849px;
    height: 1200px;
  }
  .arc__text {
    font-family: "Ultra", "Alfa Slab One", serif;
    font-size: 112px;
    fill: var(--white);
    letter-spacing: 2px;
  }
  .seal {
    position: absolute;
    left: 368px;
    top: 1030px;
    width: 124px;
    height: 124px;
    border-radius: 50%;
    background: var(--wine);
    box-shadow: 3px 4px 5px var(--shadow);
  }
</style>
</head>
<body>
<main class="poster">
  <div class="poster__backdrop" role="img" aria-label="Faceted mauve geometric background of overlapping translucent triangles"></div>

  <svg class="ribbon" viewBox="0 0 849 320" aria-hidden="true">
    <defs>
      <filter id="ribbon-shadow" x="-10%" y="-10%" width="130%" height="140%">
        <feDropShadow dx="4" dy="6" stdDeviation="3" flood-color="#461226" flood-opacity="0.55"/>
      </filter>
    </defs>
    <g fill="#ffffff" filter="url(#ribbon-shadow)">
      <polygon points="72,146 215,146 215,262 332,302 74,300 150,222"/>
      <polygon points="777,146 612,146 612,262 520,302 775,300 700,222"/>
      <rect x="215" y="107" width="397" height="133"/>
    </g>
  </svg>
  <h1 class="ribbon__label">DO MORE</h1>

  <p class="line line--of">OF</p>
  <p class="line line--what">WHAT</p>

  <div class="makes">
    <span class="makes__rule"></span>
    <span class="makes__word">MAKES</span>
    <span class="makes__rule"></span>
  </div>

  <p class="line line--you">YOU</p>

  <svg class="arc" viewBox="0 0 849 1200" aria-label="HAPPY">
    <defs>
      <path id="happy-curve" d="M 120,890 Q 425,1030 735,880"/>
      <filter id="word-shadow" x="-10%" y="-20%" width="130%" height="150%">
        <feDropShadow dx="4" dy="5" stdDeviation="3" flood-color="#461226" flood-opacity="0.55"/>
      </filter>
    </defs>
    <text class="arc__text" filter="url(#word-shadow)">
      <textPath href="#happy-curve" startOffset="50%" text-anchor="middle">HAPPY</textPath>
    </text>
  </svg>

  <div class="seal" aria-hidden="true"></div>
</main>
</body>
</html>
```